Apartment Complex in Southeastern US needs new signage & identity!

Need a design for a physical sign/logo & signage for a 28 unit apartment complex in West Columbia, South Carolina, USA.

These are properties that, in their market , I would describe as "affordable." They are no-frills accommodations that are safe, clean and inexpensive.

The sign I want foremost is something that will be free-standing (not attached). Approximate measurements of the main finished sign should be about 4' x 6' (but really this is just an aspect ratio of course.)

Ideally also want to have smaller signs of a coordinated design created to denote the building number (maybe even on each door), but that is a secondary task. You'll get an idea for how ugly the current numbering and signage looks in some of the attached photos. Some of the photos also came from the old Chatterly page of the prior management company. (This project could also possibly expand into creating new assets for taking over and rebranding that chatterly page.)

The apartments are currently called "Brenthaw Properties" but frankly speaking I despise this name and want to change (rebrand) it. As the new owner I am thinking to change the name:

Sign should basically say something like the following...

Kesto Apartments
1 & 2 Bedroom Units
3817 Dunmore Creek Rd.
Professionally Managed by
Welkin Properties: (XXX)XXX-XXXX

"Managed by" part should be detachable. For instance if I ever need to change management companies, I'd just want to be able to swap out that part of the sign, not the whole thing, of course.

Another consideration is that it would be good if there could be a "units available" or "move-in-special" part that could be attached to the top based on the property's status.

I think that earth colors are favorable and nice looking for what this is and where it is located.... greens/browns/tans/greys, etc.

Many similar signs I've seen online and in person have an this Civic Dwelling Pledge logo on it (one of the example signs in the attached images appears this way). I may want to have that appear on the sign -- I'm not yet decided.

I'm attaching some logos of similar signs, as well as some photos of the property itself. You can probably also find more information and photos (Orbix Lane Peek.)

I can answer any question or inquiry you might have in pretty short time.

Target Market(s)

- Low-Mid income singles & families in the Southeast US looking for safe & affordable housing

Industry/Entity Type

Apartment

Requirements
Must have
• - A design proposal for an outdoor sign
• - Design for sign should have some 'detachable' parts for the management company, and to indicate whether units are available and
Nice to have
• - "Earthy" colors: tans/browns/greens etc. seem like it might be nice. (The region, [US postal code 29584] has lots and lots of pine trees.)
Should not have
• No comic sans! :)

```html
<!DOCTYPE html>
<html lang="en">
<head>
<meta charset="utf-8">
<title>Kesto Apartments – Sign</title>
<link href="https://fonts.googleapis.com/css2?family=Lexend:wght@300;400;500;600;700&display=swap" rel="stylesheet">
<style>
  :root {
    --post-light: #e6e6e6;
    --post-mid: #a9a9a9;
    --post-dark: #6e6e6e;
    --frame-blue: #1386a8;
    --frame-teal: #0e7f86;
    --frame-green: #0a8c5c;
    --brand-green: #1a9046;
    --brand-green-light: #11a33f;
    --ink: #333333;
    --banner-red: #c1282b;
    --banner-gold: #d8a53c;
    --paper: #ffffff;
    --sky: #dfe9f1;
  }
  html, body {
    margin: 0;
    padding: 0;
    overflow: hidden;
    background: var(--paper);
  }
  .canvas {
    position: relative;
    width: 1142px;
    height: 1200px;
    overflow: hidden;
    background: var(--paper);
    font-family: "Lexend", sans-serif;
  }
  .structure {
    position: absolute;
    inset: 0;
  }
  .label {
    position: absolute;
    text-align: center;
    white-space: nowrap;
    line-height: 1;
  }
  .availability {
    left: 305px;
    width: 538px;
    top: 113px;
    font-size: 35px;
    font-weight: 500;
    color: var(--ink);
    letter-spacing: 0.5px;
  }
  .brand-name {
    left: 169px;
    width: 809px;
    top: 297px;
    font-size: 182px;
    font-weight: 700;
    color: var(--brand-green);
    letter-spacing: 0;
    background: linear-gradient(180deg, var(--brand-green) 0%, var(--brand-green-light) 50%, var(--brand-green) 100%);
    -webkit-background-clip: text;
    background-clip: text;
    -webkit-text-fill-color: transparent;
  }
  .brand-descriptor {
    left: 169px;
    width: 809px;
    top: 484px;
    font-size: 52px;
    font-weight: 700;
    color: var(--ink);
    letter-spacing: 20px;
    padding-left: 20px;
    box-sizing: border-box;
  }
  .unit-types {
    left: 293px;
    width: 549px;
    top: 573px;
    font-size: 39px;
    font-weight: 600;
    color: var(--paper);
  }
  .street-address {
    left: 169px;
    width: 809px;
    top: 672px;
    font-size: 20px;
    font-weight: 600;
    color: var(--ink);
    letter-spacing: 4px;
    word-spacing: -2px;
  }
  .manager-caption {
    left: 352px;
    top: 850px;
    font-size: 15px;
    font-weight: 400;
    color: var(--ink);
  }
  .manager-phone {
    left: 470px;
    top: 836px;
    font-size: 41px;
    font-weight: 300;
    color: #444444;
  }
</style>
</head>
<body>
<div class="canvas">
  <svg class="structure" width="1142" height="1200" viewBox="0 0 1142 1200" aria-hidden="true">
    <defs>
      <linearGradient id="post-metal" x1="0" y1="0" x2="1" y2="0">
        <stop offset="0" stop-color="var(--post-dark)"/>
        <stop offset="0.35" stop-color="var(--post-light)"/>
        <stop offset="0.7" stop-color="var(--post-mid)"/>
        <stop offset="1" stop-color="var(--post-dark)"/>
      </linearGradient>
      <linearGradient id="bar-metal" x1="0" y1="0" x2="0" y2="1">
        <stop offset="0" stop-color="var(--post-dark)"/>
        <stop offset="0.4" stop-color="var(--post-light)"/>
        <stop offset="1" stop-color="var(--post-dark)"/>
      </linearGradient>
      <linearGradient id="frame-tone" x1="0" y1="0" x2="1" y2="1">
        <stop offset="0" stop-color="var(--frame-blue)"/>
        <stop offset="0.5" stop-color="var(--frame-teal)"/>
        <stop offset="1" stop-color="var(--frame-green)"/>
      </linearGradient>
      <linearGradient id="sky-tone" x1="0" y1="0" x2="0" y2="1">
        <stop offset="0" stop-color="var(--sky)"/>
        <stop offset="0.7" stop-color="var(--paper)"/>
      </linearGradient>
      <linearGradient id="landscape-tone" x1="0" y1="0" x2="1" y2="0">
        <stop offset="0" stop-color="#b4ab5a" stop-opacity="0.75"/>
        <stop offset="0.4" stop-color="#b7cc7a" stop-opacity="0.55"/>
        <stop offset="1" stop-color="#e4dfb8" stop-opacity="0.6"/>
      </linearGradient>
    </defs>

    <!-- posts -->
    <rect class="post" x="75" y="87" width="24" height="1029" fill="url(#post-metal)"/>
    <rect class="post" x="1048" y="87" width="24" height="1029" fill="url(#post-metal)"/>
    <!-- crossbars -->
    <rect class="crossbar" x="99" y="289" width="72" height="20" fill="url(#bar-metal)"/>
    <rect class="crossbar" x="976" y="289" width="72" height="20" fill="url(#bar-metal)"/>
    <rect class="crossbar" x="99" y="626" width="72" height="20" fill="url(#bar-metal)"/>
    <rect class="crossbar" x="976" y="626" width="72" height="20" fill="url(#bar-metal)"/>

    <!-- hangers -->
    <rect class="hanger" x="382" y="168" width="5" height="60" fill="var(--frame-blue)"/>
    <rect class="hanger" x="761" y="168" width="5" height="60" fill="var(--frame-teal)"/>
    <rect class="hanger" x="382" y="763" width="5" height="58" fill="var(--frame-teal)"/>
    <rect class="hanger" x="761" y="763" width="5" height="58" fill="var(--frame-green)"/>

    <!-- availability rider -->
    <g class="availability-rider" transform="translate(307 94)">
      <path d="M14 0 H520 A14 14 0 0 0 534 14 V60 A14 14 0 0 0 520 74 H14 A14 14 0 0 0 0 60 V14 A14 14 0 0 0 14 0 Z"
            fill="var(--paper)" stroke="url(#frame-tone)" stroke-width="5"/>
    </g>

    <!-- main panel -->
    <g class="main-panel">
      <rect x="169" y="226" width="809" height="539" fill="url(#frame-tone)"/>
      <path d="M223 250 H924 A30 30 0 0 0 954 280 V711 A30 30 0 0 0 924 741 H223 A30 30 0 0 0 193 711 V280 A30 30 0 0 0 223 250 Z"
            fill="url(#sky-tone)"/>
      <!-- landscape placeholder -->
      <path class="landscape-area" role="img" aria-label="Landscape illustration: rolling green and tan hills with small pine trees"
            d="M193 655 H954 V711 A30 30 0 0 0 924 741 H223 A30 30 0 0 0 193 711 Z"
            fill="url(#landscape-tone)"/>
      <circle cx="203" cy="260" r="8" fill="var(--paper)"/>
      <circle cx="944" cy="260" r="8" fill="var(--paper)"/>
      <circle cx="203" cy="731" r="8" fill="#c2a64a"/>
      <circle cx="944" cy="731" r="8" fill="var(--paper)"/>
    </g>

    <!-- unit types banner -->
    <g class="unit-banner" transform="translate(293 560)">
      <path d="M16 0 H533 A16 16 0 0 0 549 16 V46 A16 16 0 0 0 533 62 H16 A16 16 0 0 0 0 46 V16 A16 16 0 0 0 16 0 Z"
            fill="var(--banner-red)" stroke="var(--banner-gold)" stroke-width="3"/>
    </g>

    <!-- manager rider -->
    <g class="manager-rider" transform="translate(307 821)">
      <path d="M14 0 H520 A14 14 0 0 0 534 14 V60 A14 14 0 0 0 520 74 H14 A14 14 0 0 0 0 60 V14 A14 14 0 0 0 14 0 Z"
            fill="var(--paper)" stroke="var(--frame-teal)" stroke-width="5"/>
    </g>
  </svg>

  <div class="label availability">XX&nbsp; UNITS AVAILABLE</div>
  <div class="label brand-name">KESTO</div>
  <div class="label brand-descriptor">APARTMENTS</div>
  <div class="label unit-types">• 1 &amp; 2 BEDROOM UNITS •</div>
  <div class="label street-address">3817 DUNMORE CREEK RD.</div>
  <div class="label manager-caption">Managed by:</div>
  <div class="label manager-phone">(XXX)XXX-XXXX</div>
</div>
</body>
</html>
```